Letterhead and Stationary for Construction Company

Brisk Current needs modern Letterhead, Envelopes and Notepad designs.

Industry/Entity Type

Construction

Colors
f78f20
34a7d8
ffffff

Requirements
Must have
• Modern looking design.

```html
<!DOCTYPE html>
<html lang="en">
<head>
<meta charset="utf-8">
<title>Brisk Current Stationery</title>
<link rel="stylesheet" href="https://fonts.googleapis.com/css2?family=Lato:wght@400;700;900&family=Parisienne&display=swap">
<style>
  :root {
    --backdrop: #67686a;
    --paper: #ffffff;
    --orange: #f07f1f;
    --blue: #1876bd;
    --ink: #222222;
    --rule: #a9a9a9;
    --muted: #cfcfcf;
  }
  * { box-sizing: border-box; margin: 0; padding: 0; }
  html, body { width: 1200px; height: 621px; overflow: hidden; }
  body { background: var(--backdrop); font-family: "Lato", sans-serif; color: var(--ink); position: relative; }

  .sheet { position: absolute; background: var(--paper); overflow: hidden; box-shadow: 3px 4px 6px rgba(0,0,0,.35); }
  .brand { position: absolute; display: flex; align-items: center; gap: 6px; }
  .brand-dot { width: 22px; height: 22px; border-radius: 50%; border: 4px solid var(--orange); }
  .brand-name { font-weight: 900; color: var(--blue); font-size: 19px; line-height: 1; letter-spacing: -.2px; white-space: nowrap; }
  .address-tag { position: absolute; border-left: 1px solid var(--blue); padding-left: 4px; font-size: 5.4px; font-weight: 700; color: #555; line-height: 1.35; white-space: nowrap; }

  .footer-band { position: absolute; left: 0; bottom: 0; width: 100%; }
  .footer-band svg { display: block; width: 100%; }
  .footer-contacts { position: absolute; left: 0; right: 0; bottom: 0; display: flex; justify-content: center; align-items: center; color: #fff; font-weight: 700; white-space: nowrap; }
  .footer-contacts .sep { margin: 0 1.6em; opacity: .9; }
  .footer-contacts .item { display: flex; align-items: center; gap: 4px; }
  .footer-contacts svg { fill: #fff; }

  /* Letterhead */
  .letterhead { left: 66px; top: 58px; width: 350px; height: 495px; }
  .letterhead .brand { left: 32px; top: 27px; }
  .letterhead .address-tag { left: 246px; top: 46px; }
  .letter { position: absolute; left: 33px; top: 122px; width: 285px; font-size: 6px; line-height: 1.38; }
  .recipient { font-size: 6.8px; line-height: 1.3; }
  .salutation { font-size: 7.8px; margin-top: 12px; margin-bottom: 5px; }
  .letter p.body { text-align: justify; margin-bottom: 7px; }
  .closing { margin-top: 10px; font-size: 6.3px; }
  .signoff { font-family: "Parisienne", cursive; color: var(--blue); font-size: 12px; margin-top: 2px; }
  .signature { width: 42px; height: 26px; margin-top: 6px; background: linear-gradient(120deg, #dfe5f2, #c9d3ea); }
  .letterhead .footer-contacts { height: 23px; font-size: 6.4px; }

  /* Notepad */
  .notepad { left: 442px; top: 58px; width: 258px; height: 360px; }
  .notepad .brand { left: 22px; top: 28px; }
  .notepad .brand-dot { width: 18px; height: 18px; border-width: 3px; }
  .notepad .brand-name { font-size: 15px; }
  .notepad .address-tag { left: 180px; top: 22px; font-size: 5px; font-weight: 400; }
  .writing-lines { position: absolute; left: 22px; top: 86px; width: 214px; }
  .writing-lines span { display: block; height: 14.6px; border-bottom: 1px solid var(--rule); }
  .notepad .footer-contacts { height: 14px; font-size: 4.3px; }

  /* Envelope front */
  .envelope-front { left: 728px; top: 58px; width: 403px; height: 176px; }
  .envelope-front .brand { left: 24px; top: 27px; }
  .envelope-front .footer-contacts { height: 19px; font-size: 5.6px; font-weight: 400; }

  /* Envelope back */
  .envelope-back { left: 728px; top: 258px; width: 403px; height: 176px; }
  .envelope-back .flap { position: absolute; left: 0; top: 0; width: 403px; height: 76px; }
  .flap-dot { position: absolute; left: 188px; top: 17px; width: 26px; height: 26px; border-radius: 50%; border: 4px solid #fff; }
  .back-name { position: absolute; left: 0; right: 0; top: 104px; text-align: center; font-weight: 900; font-size: 17px; color: var(--muted); letter-spacing: -.2px; }
</style>
</head>
<body>

<section class="sheet letterhead">
  <div class="brand"><span class="brand-dot"></span><span class="brand-name">Brisk Current</span></div>
  <div class="address-tag">718 Harbor Ridge Ave<br>Coral Point, FL 33410</div>

  <div class="letter">
    <div class="recipient">Mr/s<br>First &amp; Last name<br>Company name<br>Address</div>
    <div class="salutation">Dear Sir</div>
    <p class="body">Lorem ipsum is simply dummy text of the printing and typesetting industry. Lorem ipsum has been the industry's standard dummy text ever since the 1500s, when an unknown printer took a galley of type and scrambled it to make a type specimen book. It was popularised in the 1960s with the release of sheets containing Lorem ipsum passages, and more recently with desktop publishing software.</p>
    <p class="body">It is a long established fact that a reader will be distracted by the readable content of a page when looking at its layout. The point of using Lorem ipsum is that it has a more-or-less normal distribution of letters, as opposed to using 'Content here, content here', making it look like readable English for every reader.</p>
    <p class="body">The point of using Lorem ipsum is that it has a more-or-less normal distribution of letters, as opposed to using 'Content here, content here', making it look like readable English. Page editors now use Lorem ipsum as their default model text, and a search will uncover many web sites still in their infancy. Various versions have evolved over the years, sometimes by accident, sometimes on purpose.</p>
    <p class="body">It is a long established fact that a reader will be distracted by the readable content of a page when looking at its layout. The point of using Lorem ipsum is that it has a more-or-less normal distribution of letters.</p>
    <div class="closing">Warm regards</div>
    <div class="signoff">Brisk Current</div>
    <div class="signature" role="img" aria-label="Handwritten signature"></div>
  </div>

  <div class="footer-band">
    <svg viewBox="0 0 350 34" preserveAspectRatio="none"><path d="M0 14 Q175 -2 350 9 L350 34 L0 34Z" fill="var(--orange)"/><path d="M0 16 Q175 2 350 12.5 L350 34 L0 34Z" fill="var(--blue)"/></svg>
  </div>
  <div class="footer-contacts">
    <span class="item"><svg width="7" height="7" viewBox="0 0 24 24"><path d="M6.6 10.8a15 15 0 0 0 6.6 6.6l2.2-2.2c.3-.3.7-.4 1-.2 1.1.4 2.3.6 3.6.6.6 0 1 .4 1 1V20c0 .6-.4 1-1 1A17 17 0 0 1 3 4c0-.6.4-1 1-1h3.5c.6 0 1 .4 1 1 0 1.3.2 2.5.6 3.6.1.3 0 .7-.2 1z"/></svg>+1-30-55512890</span>
    <span class="sep">|</span>
    <span class="item"><svg width="7" height="6" viewBox="0 0 24 20"><path d="M2 2h20v16H2z" fill="#fff"/><path d="M2 3l10 7 10-7" stroke="var(--blue)" stroke-width="2" fill="none"/></svg>hello@briskcurrent.biz</span>
    <span class="sep">|</span>
    <span class="item"><svg width="7" height="7" viewBox="0 0 24 24"><circle cx="12" cy="12" r="10"/></svg>www.briskcurrent.biz</span>
  </div>
</section>

<section class="sheet notepad">
  <div class="brand"><span class="brand-dot"></span><span class="brand-name">Brisk Current</span></div>
  <div class="address-tag">718 Harbor Ridge Ave<br>Coral Point, FL 33410</div>
  <div class="writing-lines">
    <span></span><span></span><span></span><span></span><span></span><span></span><span></span><span></span><span></span><span></span><span></span><span></span><span></span><span></span><span></span><span></span><span></span><span></span><span></span>
  </div>
  <div class="footer-band">
    <svg viewBox="0 0 258 22" preserveAspectRatio="none"><path d="M0 7 Q129 -2 258 5 L258 22 L0 22Z" fill="var(--orange)"/><path d="M0 9 Q129 0 258 8 L258 22 L0 22Z" fill="var(--blue)"/></svg>
  </div>
  <div class="footer-contacts">
    <span class="item">+1-30-55512890</span><span class="sep">|</span>
    <span class="item">hello@briskcurrent.biz</span><span class="sep">|</span>
    <span class="item">www.briskcurrent.biz</span>
  </div>
</section>

<section class="sheet envelope-front">
  <div class="brand"><span class="brand-dot"></span><span class="brand-name">Brisk Current</span></div>
  <div class="footer-band">
    <svg viewBox="0 0 403 28" preserveAspectRatio="none"><path d="M0 10 Q200 -2 403 8 L403 28 L0 28Z" fill="var(--orange)"/><path d="M0 12 Q200 1 403 11 L403 28 L0 28Z" fill="var(--blue)"/></svg>
  </div>
  <div class="footer-contacts">
    <span class="item"><svg width="6" height="8" viewBox="0 0 24 32"><path d="M12 0a11 11 0 0 0-11 11c0 8 11 21 11 21s11-13 11-21A11 11 0 0 0 12 0zm0 15a4 4 0 1 1 0-8 4 4 0 0 1 0 8z" fill="var(--orange)"/></svg>718 Harbor Ridge Ave, Coral Point, FL 33410</span>
  </div>
</section>

<section class="sheet envelope-back">
  <svg class="flap" viewBox="0 0 403 76"><path d="M0 0 H403 L398 18 Q390 48 310 60 L201 74 L92 60 Q13 48 5 18 Z" fill="var(--blue)"/></svg>
  <div class="flap-dot"></div>
  <div class="back-name">Brisk Current</div>
</section>

</body>
</html>
```